Juice Label for Hispanic Customer Demographic

We need a label design for two related Juice items. Brand name will be "Cafrelo" The first item is a Lemon Juice Blend and the second is a lime juice. We would like to see designs that focus on a target market that is mainly first and second generation Hispanic immigrants. Heavily Spanish speaking and price conscious.

Product will be packaged in 32 oz flip to bottle with wrap around label. Both SKU’s will have the same size and design with one showing Lemons and the other showing Limes similar to the examples attached. The bottle will be green with a green cap for the lime juice and a yellow cap for the lemon juice.

I have attached Dielines and some images of a similar product for reference.

Target Market(s)

Hispanic shopper, mainly first and second generation immigrants. Heavily Spanish speaking demographic. Price conscious.

Industry/Entity Type

Grocery Store

Font styles to use
Sans Serif

Colors
ffcf3e
abd036
fbf289
fbee3e

Requirements
Must have
• Product Name—
• • “Cafrelo Lemon Juice Blend” -- 54% Juice
• • “Cafrelo Lime Juice “-- 25% Juice
• Please include copy-
• Note: Product name and required copy below should be in English. Additional copy can be either English or Spanish.
• • “Made in the USA”
• • “From Concentrate”
• • “Naturally Reconstituted”
• • “Refrigerate after opening”
• • “Shake Well!”
• • “Net 32 Fl OZ (1QT) 946 ml”
• Please include a space for the nutrition facts should be :
• 4 8/10 cm H x 3 8/10 cm W.
• Include a white space for the scan bar 1/7/10 cm H x 3/2/10 cm W. (?? Dimensions)
• Please use ingredient lists as below-
• Lemon Juice--
• INGREDIENTS: FILTERED WATER, LEMON
• JUICE CONCENTRATE, CITRIC ACID, ESTER
• GUM, LEMON OIL, SODIUM BENZOATE (AS
• PRESERVATIVE), SODIUM BISULFITE (AS
• PRESERVATIVE).
• Lime Juice--
• INGREDIENTS: FILTERED WATER, LIME JUICE CONCENTRATE, CITRIC ACID,
• ESTER GUM, LIME OIL, SODIUM BENZOATE (AS PRESERVATIVE), SODIUM BISULFITE (AS A PRESERVATIVE)
Nice to have
• Would like to have an image of fruit very prominent in the design. This image can be either a drawing or a photograph.

```html
<!DOCTYPE html>
<html lang="en">
<head>
<meta charset="utf-8">
<title>Cafrelo Juice Labels</title>
<link href="https://fonts.googleapis.com/css2?family=Arvo:wght@400;700&family=Lora&family=Ultra&family=Open+Sans:wght@400;600;700&display=swap" rel="stylesheet">
<style>
  :root {
    --page-bg: #d8d8d8;
    --white: #ffffff;
    --ink: #111111;
    --grey-text: #555555;
    --brand-green: #abd036;
    --concentrate-green: #3aa52f;
    --lemon-band: #fbee3e;
    --lemon-accent: #ffcf3e;
    --lemon-soft: #fbf289;
    --lime-band: #abd036;
    --lime-accent: #abd036;
    --lime-soft: #cfe57f;
  }
  * { box-sizing: border-box; margin: 0; padding: 0; }
  html, body { width: 1200px; height: 1014px; overflow: hidden; }
  body { background: var(--page-bg); position: relative; font-family: "Open Sans", sans-serif; }

  .label {
    position: absolute; left: 188px; width: 830px; height: 404px;
    background: var(--white);
    box-shadow: 4px 8px 10px rgba(0,0,0,0.35);
    overflow: hidden;
  }
  .label--lemon { top: 63px; --band: var(--lemon-band); --accent: var(--lemon-accent); --soft: var(--lemon-soft); }
  .label--lime  { top: 533px; --band: var(--lime-band); --accent: var(--lime-accent); --soft: var(--lime-soft); }

  .citrus-decor { position: absolute; top: 0; height: 160px; }
  .citrus-decor--left  { left: 0; width: 292px; background: radial-gradient(ellipse at 40% 45%, var(--soft) 0%, var(--soft) 45%, rgba(255,255,255,0) 80%); }
  .citrus-decor--right { right: 0; width: 313px; background: radial-gradient(ellipse at 60% 45%, var(--soft) 0%, var(--soft) 45%, rgba(255,255,255,0) 80%); }

  .brand {
    position: absolute; top: 50px; left: 0; width: 100%; text-align: center;
    font-family: "Arvo", serif; font-weight: 400; font-size: 48px; line-height: 1;
    color: var(--brand-green); letter-spacing: 1px;
  }
  .product-name {
    position: absolute; top: 110px; left: 0; width: 100%; text-align: center;
    font-family: "Lora", serif; font-size: 25px; color: var(--grey-text); letter-spacing: 0.5px;
  }

  .band { position: absolute; top: 160px; left: 0; width: 100%; height: 244px; background: var(--band); }

  .care-note {
    position: absolute; left: 0; width: 230px; text-align: center;
    font-size: 11.5px; line-height: 13px; color: var(--ink); text-transform: uppercase;
  }
  .care-note--top { top: 167px; }
  .care-note--bottom { top: 378px; }
  .nutrition-space {
    position: absolute; left: 46px; top: 197px; width: 138px; height: 173px;
    background: var(--white); border: 2px solid var(--ink);
  }

  .front-panel { position: absolute; left: 253px; top: 188px; width: 326px; height: 216px; background: var(--white); }
  .fruit-image {
    position: absolute; left: 10px; top: 32px; width: 180px; height: 160px; border-radius: 50%;
    background: radial-gradient(circle at 50% 50%, var(--accent) 0%, var(--soft) 55%, rgba(255,255,255,0) 72%);
  }
  .from-concentrate {
    position: absolute; right: 7px; top: 7px;
    font-size: 14px; font-weight: 700; color: var(--concentrate-green); letter-spacing: 0.3px;
  }
  .juice-percent {
    position: absolute; right: 8px; top: 46px;
    font-family: "Ultra", serif; font-size: 46px; line-height: 1; color: var(--accent);
  }
  .juice-word {
    position: absolute; right: 14px; top: 108px;
    font-family: "Ultra", serif; font-size: 34px; line-height: 1; color: var(--accent);
  }
  .made-in, .net-content {
    position: absolute; right: 13px; font-size: 11.5px; font-weight: 700; color: var(--ink);
  }
  .made-in { top: 175px; }
  .net-content { top: 190px; }

  .ingredients {
    position: absolute; left: 610px; top: 189px; width: 199px;
    font-size: 9.6px; line-height: 12.8px; font-weight: 600; color: var(--ink);
    text-align: justify; text-transform: uppercase;
  }
  .ingredients strong { font-weight: 700; }
  .barcode-space { position: absolute; left: 652px; top: 262px; width: 116px; height: 61px; background: var(--white); }
</style>
</head>
<body>

<section class="label label--lemon">
  <div class="citrus-decor citrus-decor--left" role="img" aria-label="Scattered translucent lemon slices"></div>
  <div class="citrus-decor citrus-decor--right" role="img" aria-label="Scattered translucent lemon slices"></div>
  <h1 class="brand">Cafrelo</h1>
  <h2 class="product-name">Lemon Juice Blend</h2>
  <div class="band"></div>
  <p class="care-note care-note--top">Naturally reconstituted<br>Shake well</p>
  <div class="nutrition-space"></div>
  <p class="care-note care-note--bottom">Refrigerate after opening</p>
  <div class="front-panel">
    <div class="fruit-image" role="img" aria-label="Photo of whole and halved lemons with leaves"></div>
    <p class="from-concentrate">FROM CONCENTRATE</p>
    <p class="juice-percent">54%</p>
    <p class="juice-word">Juice</p>
    <p class="made-in">MADE IN THE USA</p>
    <p class="net-content">Net 32 fl OZ (1QT) 946 ml</p>
  </div>
  <p class="ingredients"><strong>Ingredients:</strong> Filtered water, lemon juice concentrate, citric acid, ester gum, lemon oil, sodium benzoate (as preservative), sodium bisulfate (as preservative).</p>
  <div class="barcode-space"></div>
</section>

<section class="label label--lime">
  <div class="citrus-decor citrus-decor--left" role="img" aria-label="Scattered translucent lime slices"></div>
  <div class="citrus-decor citrus-decor--right" role="img" aria-label="Scattered translucent lime slices"></div>
  <h1 class="brand">Cafrelo</h1>
  <h2 class="product-name">Lime Juice</h2>
  <div class="band"></div>
  <p class="care-note care-note--top">Naturally reconstituted<br>Shake well</p>
  <div class="nutrition-space"></div>
  <p class="care-note care-note--bottom">Refrigerate after opening</p>
  <div class="front-panel">
    <div class="fruit-image" role="img" aria-label="Photo of whole and halved limes with leaves"></div>
    <p class="from-concentrate">FROM CONCENTRATE</p>
    <p class="juice-percent">25%</p>
    <p class="juice-word">Juice</p>
    <p class="made-in">MADE IN THE USA</p>
    <p class="net-content">Net 32 fl OZ (1QT) 946 ml</p>
  </div>
  <p class="ingredients"><strong>Ingredients:</strong> Filtered water, lemon juice concentrate, citric acid, ester gum, lemon oil, sodium benzoate (as preservative), sodium bisulfate (as preservative).</p>
  <div class="barcode-space"></div>
</section>

</body>
</html>
```